Geschäftspapiere für Hersteller von Werkstattausrüstung
Zielgruppe
Werkstattausrüstung (Hebebühnen, Achsmessgeräte, Wuchtmaschinen etc.) Zielgruppe Kfz Werkstätte

```html
<!DOCTYPE html>
<html lang="de">
<head>
<meta charset="utf-8">
<title>Geschäftspapiere – Berger &amp; Lindt</title>
<link href="https://fonts.googleapis.com/css2?family=Source+Sans+3:wght@300;400;600;700&display=swap" rel="stylesheet">
<style>
:root{
  --bg:#e5e5e5;
  --paper:#ffffff;
  --green-dark:#006b4f;
  --green-light:#8cc63f;
  --band:#ebf4dc;
  --ink:#2a2a2a;
  --wash:#eef4ee;
}
*{margin:0;padding:0;box-sizing:border-box}
html,body{width:1200px;height:1200px;overflow:hidden;background:var(--bg);font-family:"Source Sans 3",sans-serif}
.stage{position:relative;width:1200px;height:1200px}
.sheet{position:absolute;top:261px;width:480px;height:678px;background:var(--paper);box-shadow:2px 3px 6px rgba(0,0,0,.18);overflow:hidden}
.sheet--blank{left:99px}
.sheet--letter{left:621px}
.brand{position:absolute;left:0;top:34px;width:100%;display:flex;justify-content:center;align-items:center;gap:10px}
.brand-dot{width:30px;height:30px;border-radius:50%;background:var(--green-dark)}
.brand-name{font-weight:600;font-size:28px;line-height:1;color:var(--green-dark)}
.sender{position:absolute;left:54px;top:113px;display:flex;align-items:center;gap:4px;font-size:4.6px;white-space:nowrap}
.sender-dot{width:7px;height:7px;border-radius:50%;background:var(--green-dark)}
.sender b{color:var(--green-dark);font-weight:700}
.sender span{color:var(--green-light)}
.fold{position:absolute;left:0;width:16px;height:1px}
.fold--one{top:239px;background:var(--green-dark)}
.fold--two{top:339px;background:var(--green-light)}
.backdrop{position:absolute;left:72px;top:265px;width:300px;height:275px;border-radius:50%;background:var(--wash);opacity:.8}
.footer{position:absolute;left:0;top:618px;width:100%;height:60px;background:var(--band)}
.footer-bar{position:absolute;left:0;bottom:0;width:100%;height:7px;background:var(--green-dark)}
.footer-dot{position:absolute;left:54px;top:16px;width:22px;height:22px;border-radius:50%;background:var(--green-dark)}
.footer-col{position:absolute;top:16px;font-size:4.8px;line-height:7.3px;color:var(--green-light);white-space:nowrap;padding-left:4px;border-left:.6px solid var(--green-dark);height:24px}
.footer-col b{color:var(--green-dark);font-weight:700;display:inline-block}
.col-company{left:97px}
.col-contact{left:184px}
.col-contact b{width:22px}
.col-register{left:266px}
.col-register b{width:42px}
.col-bank{left:372px}
.col-bank b{width:15px}
.letter{position:absolute;left:54px;top:0;width:398px;color:var(--ink);font-size:7.7px;line-height:10.25px;font-weight:300}
.letter-date{position:absolute;right:25px;top:251px;font-size:7.7px;font-weight:300;color:var(--ink)}
.letter-subject{position:absolute;top:280px;font-weight:600;color:#111}
.letter-salutation{position:absolute;top:321px}
.letter-body{position:absolute;top:342px}
.letter-body p+p{margin-top:10.25px}
.letter-closing{position:absolute;top:475px}
.letter-signature{position:absolute;top:493px;left:0;width:100px;height:22px;background:linear-gradient(90deg,rgba(28,28,140,.14),rgba(28,28,140,.05))}
.letter-name{position:absolute;top:526px}
</style>
</head>
<body>
<main class="stage">

  <section class="sheet sheet--blank">
    <div class="backdrop" role="img" aria-label="Blasses grünes Hintergrundmotiv"></div>
    <header class="brand">
      <div class="brand-dot"></div>
      <span class="brand-name">Berger &amp; Lindt</span>
    </header>
    <div class="sender"><i class="sender-dot"></i><b>BERGER &amp; LINDT GmbH &amp; Co. KG</b> <span>• Am Werkhof 14 • 64999 Talbach</span></div>
    <i class="fold fold--one"></i><i class="fold fold--two"></i>
    <footer class="footer">
      <i class="footer-dot"></i>
      <div class="footer-col col-company"><b>BERGER &amp; LINDT GMBH &amp; CO. KG</b><br>Am Werkhof 14<br>64999 Talbach</div>
      <div class="footer-col col-contact"><b>Telefon:</b> +49 (0) 6000 / 123 45 0<br><b>E-Mail:</b> info@berger-lindt.de<br><b>Internet:</b> www.berger-lindt.de</div>
      <div class="footer-col col-register"><b>Registergericht:</b> Amtsgericht Talbach<br><b>Registernummer:</b> HRA 10000<br><b>USt-IdNr.</b> DE000111222</div>
      <div class="footer-col col-bank"><b>Bank:</b> Muster Bank<br><b>IBAN:</b> DE00 1234 5678 9000 1111 22<br><b>BIC:</b> ABCDEFGH</div>
      <i class="footer-bar"></i>
    </footer>
  </section>

  <section class="sheet sheet--letter">
    <div class="backdrop" role="img" aria-label="Blasses grünes Hintergrundmotiv"></div>
    <header class="brand">
      <div class="brand-dot"></div>
      <span class="brand-name">Berger &amp; Lindt</span>
    </header>
    <div class="sender"><i class="sender-dot"></i><b>BERGER &amp; LINDT GmbH &amp; Co. KG</b> <span>• Am Werkhof 14 • 64999 Talbach</span></div>
    <i class="fold fold--one"></i><i class="fold fold--two"></i>
    <div class="letter-date">Musterstadt, 18.04.2022</div>
    <article class="letter">
      <p class="letter-subject">Ich bin eine Betreffzeile mit Blindtext. Ich bin eine Betreffzeile mit Blindtext.</p>
      <p class="letter-salutation">Sehr geehrte Damen und Herren,</p>
      <div class="letter-body">
        <p>ich bin Blindtext. Von Geburt an. Es hat lange gedauert, bis ich begriffen habe, was es bedeutet, ein blinder Text zu sein: Man macht keinen Sinn. Man wirkt hier und da aus dem Zusammenhang gerissen. Oft wird man gar nicht erst gelesen. Aber bin ich deshalb ein schlechter Text? Ich weiß, dass ich nie die Chance haben werde im Stern zu erscheinen. Aber bin ich darum weniger wichtig? Ich bin blind! Aber ich bin gerne Text. Und sollten Sie mich jetzt tatsächlich zu Ende lesen, dann habe ich etwas geschafft, was den meisten „normalen“ Texten nicht gelingt. Ich bin Blindtext.</p>
        <p>Und sollten Sie mich jetzt tatsächlich zu Ende lesen, dann habe ich etwas geschafft, was den meisten „normalen“ Texten nicht gelingt. Ich bin Blindtext. Von Geburt an. Es hat lange gedauert, bis ich begriffen habe, was es bedeutet, ein blinder Text zu sein: Man macht keinen Sinn. Man wirkt hier und da aus dem Zusammenhang gerissen. Oft wird man gar nicht erst gelesen. Aber bin ich deshalb ein schlechter Text? Ich weiß, dass ich nie die Chance haben werde im Stern zu erscheinen. Aber bin ich darum weniger wichtig? Ich bin blind! Aber ich bin gerne Text. Und sollten Sie mich jetzt tatsächlich zu Ende lesen, dann habe ich etwas geschafft, was den meisten „normalen“ Texten nicht gelingt.</p>
      </div>
      <p class="letter-closing">Mit freundlichen Grüßen</p>
      <div class="letter-signature" role="img" aria-label="Handschriftliche Unterschrift"></div>
      <p class="letter-name">Max Mustermann</p>
    </article>
    <footer class="footer">
      <i class="footer-dot"></i>
      <div class="footer-col col-company"><b>BERGER &amp; LINDT GMBH &amp; CO. KG</b><br>Am Werkhof 14<br>64999 Talbach</div>
      <div class="footer-col col-contact"><b>Telefon:</b> +49 (0) 6000 / 123 45 0<br><b>E-Mail:</b> info@berger-lindt.de<br><b>Internet:</b> www.berger-lindt.de</div>
      <div class="footer-col col-register"><b>Registergericht:</b> Amtsgericht Talbach<br><b>Registernummer:</b> HRA 10000<br><b>USt-IdNr.</b> DE000111222</div>
      <div class="footer-col col-bank"><b>Bank:</b> Muster Bank<br><b>IBAN:</b> DE00 1234 5678 9000 1111 22<br><b>BIC:</b> ABCDEFGH</div>
      <i class="footer-bar"></i>
    </footer>
  </section>

</main>
</body>
</html>
```